Summit Medals & Plaques Business Card

Business card designed to include new logo and colour scheme.
Have attached copy of old business card for details.
Simple and Elegant Layout.
Business card should look professional & the logo should be the main element of the card
Must have the similar colour scheme to the LOGO. Orange & Blue
Target Market - Schools, Clubs, Business, Sporting Organisations & Corporate

Target Market(s)

Schools, Clubs, Business, Sporting Organisations & Corporate

Industry/Entity Type

Business

Contact Information for Business Card

Attached old business card

Font styles to use
Sans Serif

Colors
f37122
0555a3

Requirements
Must have
• Simple and Elegant Layout
• Must have the similar colour scheme to the LOGO. Orange & Blue
• Social media information
• Facebook - summitmedalsplaques
• Instagram - summitmedalsplaques
• Twitter - summit_medals

```html
<!DOCTYPE html>
<html lang="en">
<head>
<meta charset="utf-8">
<title>Summit Medals &amp; Plaques – Business Card</title>
<link rel="stylesheet" href="https://fonts.googleapis.com/css2?family=Open+Sans:wght@400;600;700&display=swap">
<style>
  :root {
    --navy: #0b3a63;
    --orange: #e94e34;
    --white: #ffffff;
    --page: #e6e8eb;
    --ink: #163d63;
  }
  * { margin: 0; padding: 0; box-sizing: border-box; }
  html, body {
    width: 1200px; height: 900px; overflow: hidden;
    background: var(--page);
    font-family: "Open Sans", Arial, sans-serif;
  }
  .card {
    position: absolute; left: 250px;
    width: 700px; height: 400px;
    border-radius: 26px; overflow: hidden;
    box-shadow: 0 10px 28px rgba(0,0,0,0.18);
  }
  .card-front { top: 30px; background: var(--white); }
  .card-back { top: 470px; background: var(--navy); }

  .badge {
    position: absolute; border-radius: 50%;
    background: var(--navy);
    display: flex; align-items: center; justify-content: center;
    text-align: center;
  }
  .badge::after {
    content: ""; position: absolute; inset: 10px;
    border-radius: 50%; border: 2px solid var(--ring, var(--white));
  }
  .badge-name {
    color: var(--orange); font-weight: 700;
    text-transform: uppercase; line-height: 1.15;
    position: relative; z-index: 1;
  }
  .card-front .badge { left: 400px; top: 36px; width: 240px; height: 240px; }
  .card-front .badge-name { font-size: 24px; width: 175px; }

  .services {
    position: absolute; left: 62px; top: 190px;
    list-style: none; color: var(--ink);
    font-size: 17px; line-height: 20px;
  }
  .services li { position: relative; padding-left: 18px; }
  .services li::before {
    content: ""; position: absolute; left: 0; top: 7px;
    width: 8px; height: 8px; border-radius: 50%; background: var(--orange);
  }

  .social {
    position: absolute; left: 430px; top: 296px;
    list-style: none; color: var(--ink);
    font-size: 14px; line-height: 22px;
  }
  .social li { display: flex; align-items: center; gap: 8px; }
  .social-label { font-weight: 600; width: 74px; }
  .social li::before {
    content: ""; width: 9px; height: 9px; border-radius: 50%;
    background: var(--orange); flex: none;
  }

  .back-art { position: absolute; inset: 0; }
  .card-back .badge {
    left: 70px; top: 112px; width: 260px; height: 260px;
    --ring: var(--orange);
  }
  .card-back .badge-name { font-size: 26px; width: 185px; }

  .contact {
    position: absolute; right: 52px; top: 40px;
    text-align: right; color: var(--white);
  }
  .contact-name {
    font-size: 27px; font-weight: 700; letter-spacing: 0.5px;
    margin-bottom: 6px;
  }
  .contact-address { font-size: 15px; line-height: 19px; margin-bottom: 8px; }
  .contact-list { list-style: none; font-size: 15px; line-height: 21px; }
  .contact-list li { display: flex; justify-content: flex-end; align-items: center; gap: 10px; }
  .contact-list svg { width: 13px; height: 13px; fill: none; stroke: var(--orange); stroke-width: 2; }
</style>
</head>
<body>

<section class="card card-front">
  <div class="badge"><span class="badge-name">Summit Medals &amp; Plaques</span></div>
  <ul class="services">
    <li>Trophies &amp; Medals</li>
    <li>Corporate Awards</li>
    <li>Name Badges</li>
    <li>Custom Medals &amp; Ribbons</li>
    <li>Honour Boards</li>
    <li>Perpetuals, Plaques &amp; Shields</li>
    <li>ID Cards</li>
    <li>Labels &amp; Signage</li>
    <li>Promotional Products</li>
  </ul>
  <ul class="social">
    <li><span class="social-label">Facebook</span>summitmedalsplaques</li>
    <li><span class="social-label">Instagram</span>summitmedalsplaques</li>
    <li><span class="social-label">Twitter</span>summit_medals</li>
  </ul>
</section>

<section class="card card-back">
  <svg class="back-art" viewBox="0 0 700 400" aria-hidden="true">
    <circle cx="60" cy="300" r="342" fill="var(--white)"/>
    <circle cx="50" cy="300" r="330" fill="var(--orange)"/>
  </svg>
  <div class="badge"><span class="badge-name">Summit Medals &amp; Plaques</span></div>

  <div class="contact">
    <p class="contact-name">RAVIN KOHLI</p>
    <p class="contact-address">Unit 2/9 Harbour Lane<br>NORTHGATE, QLD 4013</p>
    <ul class="contact-list">
      <li>07 5550 1827
        <svg viewBox="0 0 14 14"><path d="M3 1l3 3-2 2c1 2 2 3 4 4l2-2 3 3-2 2C6 13 1 8 1 3z"/></svg></li>
      <li>075550 7041
        <svg viewBox="0 0 14 14"><rect x="3" y="1" width="8" height="4"/><rect x="1" y="5" width="12" height="6"/><rect x="3" y="9" width="8" height="4"/></svg></li>
      <li>0491 570 156
        <svg viewBox="0 0 14 14"><rect x="3.5" y="1" width="7" height="12" rx="1.5"/></svg></li>
      <li>ravin@summitmedals.com.au
        <svg viewBox="0 0 14 14"><rect x="1" y="3" width="12" height="8"/><path d="M1 3l6 5 6-5"/></svg></li>
      <li>www.summitmedals.com.au
        <svg viewBox="0 0 14 14"><circle cx="7" cy="7" r="6"/><path d="M1 7h12M7 1c3 3 3 9 0 12M7 1c-3 3-3 9 0 12"/></svg></li>
    </ul>
  </div>
</section>

</body>
</html>
```